Motorcycle dealer home page design (Lone Canyon Cycle Depot - 4341)

We need a home page design only (no coding necessary) for a motorcycle dealer. He wants the theme to be Modern-Industrial with vintage details. Please read the requirements below.

Client likes http://www.pelbrookridgeriders.example/ and wants a similar layout.

Dealer info:
Lone Canyon Cycle Depot (logo attached)
210.555.0147
628 W Maple Crest Dr Ste 307
San Antonio, TX 78299
Hours
Sun-Mon: Closed
Tue-Sat: 9a – 6p

Slideshow images - I've attached a few so you can see his inventory, it may help with the design

Call-to-action buttons:
Financing
Sell Your Bike
View Inventory

Theme: Modern-Industrial with Vintage details
Main background: Artistic or vintage image of motorcycle (see link for examples from client: http://instagram.com/chromeandember#)
Content background: likes the use of 'black wood' on http://www.pelbrookridgeriders.example - find a way to incorporate the wood background somewhere on the design

Accent Colors: Black, white and pops of red
Featured Vehicles location: Middle (in between the call-to-action buttons and the verbiage)
Social Networking: Facebook, Instagram

Client likes http://www.pelbrookridgeriders.example/ and wants a similar layout:
-wants the navigation bar above the banner/header
-wants the logo centered in the banner/header (open to the placement of the phone number, address and social media icons, as long as they show in the banner)
-wants to leave gaps between the sections so the background is visible

Attachments:
-layout that the client provided (LCD_HOME_PAGE)
-logo (LCD_BLACK & LCD_W)
-psd file showing the typical layout used (sample-site) - ONLY A SUGGESTION!
-a few slideshow images to show client's inventory (the rest of the files)

Please let me know if you have any questions and thank you in advance for your work.

Thank you all for your wonderful mockups. I've sent them to the client and am awaiting the response. I will keep you all updated. Best regards, Delphine

Thank you all, I am just waiting for feedback from the client. I will post the feedback as soon as I get a response from the client. Best regards, Delphine

```html
<!DOCTYPE html>
<html lang="en">
<head>
<meta charset="utf-8">
<title>Lone Canyon Cycle Depot – Home</title>
<link href="https://fonts.googleapis.com/css2?family=Roboto+Condensed:wght@400;700&family=Roboto:wght@400;700&display=swap" rel="stylesheet">
<style>
:root{
  --ink:#ffffff;
  --ink-soft:#d6d6d6;
  --red:#d2232a;
  --topbar:rgba(20,20,20,.6);
  --plank-a:#3b3b3b;
  --plank-b:#333333;
  --seam:#1c1c1c;
  --slate:#4b4b4b;
  --footer:#303030;
  --base:#232323;
  --line:rgba(255,255,255,.75);
  --paper:#f4f4f4;
  --icon:#8c8c8c;
}
*{box-sizing:border-box;margin:0;padding:0}
html,body{width:867px;height:1200px;overflow:hidden}
body{position:relative;background:var(--base);font-family:'Roboto Condensed',Arial,sans-serif;color:var(--ink)}
.abs{position:absolute}

/* hero backdrop */
.hero-backdrop{left:0;top:0;width:867px;height:522px;
  background:
    radial-gradient(ellipse 55% 45% at 88% 72%,rgba(10,10,10,.85) 0%,rgba(10,10,10,0) 100%),
    radial-gradient(ellipse 40% 35% at 10% 80%,rgba(15,15,15,.7) 0%,rgba(15,15,15,0) 100%),
    linear-gradient(160deg,#7b7b7b 0%,#5e5e5e 35%,#3c3c3c 70%,#262626 100%)}
.topbar{left:0;top:0;width:867px;height:27px;background:var(--topbar)}
.contact-item{top:8px;font-size:10px;color:var(--ink-soft);display:flex;align-items:center;gap:6px}
.social-row{display:flex;align-items:center}
.header-social{right:112px;top:6px;gap:12px}
.header-social .social-dot{width:15px;height:15px;border-radius:50%;background:var(--icon)}

.brand-mark{left:368px;top:52px;width:130px;text-align:center;font-weight:700;font-size:10px;line-height:12px;letter-spacing:.5px;color:var(--ink)}

.main-nav{left:113px;top:102px;width:640px;height:26px;display:flex;border:1px solid var(--line)}
.main-nav a{flex:1;display:flex;align-items:center;justify-content:center;font-size:9px;color:var(--ink);text-decoration:none;border-left:1px solid var(--line)}
.main-nav a:first-child{border-left:0;color:var(--red)}

.banner{left:113px;top:148px;width:640px;height:240px;background:linear-gradient(100deg,#9a9a9a 0%,#5a5a5a 22%,#161616 45%,#262626 70%,#5c5c5c 90%,#7a7a7a 100%)}
.banner-title{left:595px;top:243px;font-size:64px;font-weight:700;line-height:64px}
.banner-sub{left:594px;top:302px;font-size:38px;line-height:42px}
.banner-tag{left:495px;top:349px;font-size:14px}

.brands-bar{left:113px;top:402px;width:640px;height:32px;border:1px solid var(--line);padding-left:8px;font-size:16px;line-height:30px;background:rgba(0,0,0,.3)}
.brand-box{top:449px;width:147px;height:53px;border:1px solid var(--line);background:#0c0c0c;display:flex;align-items:center;justify-content:center;font-size:24px;font-weight:700}

/* wood planks */
.wood{background:
  repeating-linear-gradient(90deg,var(--seam) 0 2px,var(--plank-a) 2px 30px,var(--plank-b) 30px 62px),
  var(--plank-a)}
.featured{left:0;top:522px;width:867px;height:241px}
.featured-shade{left:0;top:522px;width:867px;height:241px;background:radial-gradient(ellipse at 50% 50%,rgba(0,0,0,0) 40%,rgba(0,0,0,.45) 100%)}
.section-title{font-size:16px;font-weight:400}
.featured-title{left:0;width:867px;top:538px;text-align:center}
.polaroid{width:108px;height:124px;background:var(--paper);padding:7px 7px 0;box-shadow:0 3px 8px rgba(0,0,0,.6)}
.polaroid-photo{width:94px;height:88px}
.polaroid-caption{color:#333;font-family:'Roboto',Arial,sans-serif;font-size:11px;text-align:center;margin-top:6px}
.pin{width:12px;height:14px;border-radius:5px;background:#cfcfcf}

/* about */
.about{left:0;top:763px;width:867px;height:297px;background:var(--slate)}
.about-title{left:113px;top:797px}
.about-photo{top:832px;width:200px;height:108px;border:1px solid #ddd}
.about-headline{left:113px;top:952px;width:425px;font-size:12px;white-space:nowrap;letter-spacing:-.15px}
.about-copy{left:113px;top:973px;width:420px;font-family:'Roboto',Arial,sans-serif;font-size:8.2px;line-height:11.3px;text-align:justify;color:var(--ink-soft)}

.cta{left:552px;width:200px;height:33px;border:1px solid #1a1a1a;display:flex;align-items:center;gap:12px;padding-left:10px;font-size:12px;font-weight:700;color:var(--ink)}
.newsletter{left:556px;top:927px;width:200px;height:96px;border:1px solid var(--line);background:#333;padding:12px 10px}
.newsletter-title{font-size:12px}
.newsletter-input{margin-top:10px;height:26px;border:1px solid var(--line);font-family:'Roboto',Arial,sans-serif;font-size:8px;font-style:italic;color:var(--ink-soft);padding:8px 8px}
.newsletter-submit{margin-top:10px;text-align:right;font-size:10px;padding-right:4px}

/* footer */
.site-footer{left:0;top:1060px;width:867px;height:105px;background:var(--footer)}
.footer-brand{left:116px;top:1108px;width:85px;text-align:center;font-size:9px;font-weight:700;line-height:11px}
.footer-links{top:1097px;font-family:'Roboto',Arial,sans-serif;font-size:8.5px;line-height:17px;list-style:none}
.footer-links li::before{content:"› ";font-weight:700}
.footer-social{right:114px;top:1109px;gap:15px}
.footer-social .social-dot{width:20px;height:20px;border-radius:50%;background:#e8e8e8}
.legal{left:0;top:1165px;width:867px;height:35px;background:var(--base)}
.legal-left{left:113px;top:1180px;font-size:8px;color:var(--ink-soft)}
.legal-right{right:114px;top:1181px;font-size:9px;color:var(--ink-soft)}
</style>
</head>
<body>

<div class="abs hero-backdrop" role="img" aria-label="Dim close-up photograph of a custom cruiser motorcycle parked by a garage door"></div>

<header>
  <div class="abs topbar"></div>
  <div class="abs contact-item" style="left:118px">
    <svg width="10" height="10" viewBox="0 0 10 10"><path d="M2 1l2 2-1 1.5c.6 1.2 1.3 1.9 2.5 2.5L7 6l2 2-1.2 1.5C4.5 9 1 5.5.5 2.2z" fill="#bbb"/></svg>210.555.0147
  </div>
  <div class="abs contact-item" style="left:205px">
    <svg width="8" height="11" viewBox="0 0 8 11"><path d="M4 0a4 4 0 0 1 4 4c0 3-4 7-4 7S0 7 0 4a4 4 0 0 1 4-4zm0 2.5a1.5 1.5 0 1 0 0 3 1.5 1.5 0 0 0 0-3z" fill="#bbb"/></svg>628 W Maple Crest Dr Ste 307,San Antonio.
  </div>
  <div class="abs social-row header-social" aria-label="Social links">
    <span class="social-dot"></span><span class="social-dot"></span><span class="social-dot"></span><span class="social-dot"></span>
  </div>

  <div class="abs brand-mark">LONE CANYON<br>CYCLE DEPOT</div>

  <nav class="abs main-nav">
    <a href="#">HOME</a><a href="#">ABOUT US</a><a href="#">INVENTORY</a><a href="#">SERVICES</a><a href="#">VECHILE FINDER</a><a href="#">CONTACT US</a>
  </nav>
</header>

<section>
  <div class="abs banner" role="img" aria-label="Slideshow photo of a chrome cruiser motorcycle front with headlight and red tail lamp"></div>
  <div class="abs banner-title">New</div>
  <div class="abs banner-sub">arrivals</div>
  <div class="abs banner-tag">The Best MotorCycle Performance</div>

  <div class="abs brands-bar">Our&nbsp; Top Brands</div>
  <div class="abs brand-box" style="left:113px">Velocita</div>
  <div class="abs brand-box" style="left:279px">Toromar</div>
  <div class="abs brand-box" style="left:444px">Ironhawk</div>
  <div class="abs brand-box" style="left:606px">Rossacorsa</div>
</section>

<section>
  <div class="abs featured wood"></div>
  <div class="abs featured-shade"></div>
  <h2 class="abs section-title featured-title">FEATURED VEHICLES</h2>

  <div class="abs polaroid" style="left:121px;top:594px;transform:rotate(9deg)">
    <div class="polaroid-photo" role="img" aria-label="Two riders on a sport motorcycle by the sea" style="background:linear-gradient(#9fb8d0,#5b6d80 60%,#2a2f36)"></div>
    <div class="polaroid-caption">Lorem Ipsum</div>
  </div>
  <div class="abs pin" style="left:181px;top:586px"></div>

  <div class="abs polaroid" style="left:288px;top:588px;transform:rotate(-15deg)">
    <div class="polaroid-photo" role="img" aria-label="Two riders on a sport motorcycle by the sea" style="background:linear-gradient(#a9c0d6,#60758a 60%,#2b3037)"></div>
    <div class="polaroid-caption">Lorem Ipsum</div>
  </div>
  <div class="abs pin" style="left:318px;top:586px"></div>

  <div class="abs polaroid" style="left:467px;top:592px;transform:rotate(6deg)">
    <div class="polaroid-photo" role="img" aria-label="Front of a black cruiser motorcycle" style="background:linear-gradient(#777,#2a2a2a 60%,#555)"></div>
    <div class="polaroid-caption">Lorem Ipsum</div>
  </div>
  <div class="abs pin" style="left:503px;top:586px"></div>

  <div class="abs polaroid" style="left:641px;top:592px;transform:rotate(-5deg)">
    <div class="polaroid-photo" role="img" aria-label="Red touring motorcycle dashboard" style="background:linear-gradient(#c23a3a,#8c1c1c 60%,#3a1414)"></div>
    <div class="polaroid-caption">Lorem Ipsum</div>
  </div>
  <div class="abs pin" style="left:672px;top:586px"></div>
</section>

<section>
  <div class="abs about"></div>
  <h2 class="abs section-title about-title">LONE CANYON CYCLE DEPOT</h2>
  <div class="abs about-photo" style="left:112px;background:linear-gradient(#c77a2c,#7a5a2e 50%,#9a9a9a)" role="img" aria-label="Rider on a winding autumn road"></div>
  <div class="abs about-photo" style="left:333px;background:linear-gradient(90deg,#8a8a8a,#2a2a2a 50%,#777)" role="img" aria-label="Chrome custom motorcycle parked outside"></div>
  <p class="abs about-headline">LOREM IPSUM IS SIMPLY DUMMY TEXT OF THE PRINTING AND TYPESETTING INDUSTRY.</p>
  <p class="abs about-copy">Lorem Ipsum is simply dummy text of the printing and typesetting industry. Lorem Ipsum has been the industry's standard dummy text ever since the 1500s, when an unknown printer took a galley of type and scrambled it to make a type specimen book. It has survived not only five centuries, but also the leap into electronic typesetting, remaining essentially unchanged.</p>

  <a class="abs cta wood" style="top:801px">
    <svg width="18" height="12" viewBox="0 0 18 12"><rect x="0" y="1" width="16" height="10" fill="#ddd"/><circle cx="8" cy="6" r="3" fill="#333"/></svg>FINANCING
  </a>
  <a class="abs cta wood" style="top:841px">
    <svg width="18" height="14" viewBox="0 0 18 14"><path d="M1 1h3l2 8h9l2-6H6" fill="none" stroke="#ddd" stroke-width="1.6"/><circle cx="7" cy="12" r="1.3" fill="#ddd"/><circle cx="14" cy="12" r="1.3" fill="#ddd"/></svg>SELL YOUR BIKE
  </a>
  <a class="abs cta wood" style="top:880px">
    <svg width="18" height="12" viewBox="0 0 18 12"><g fill="#ddd"><rect x="0" y="0" width="3" height="2"/><rect x="5" y="0" width="11" height="2"/><rect x="0" y="5" width="3" height="2"/><rect x="5" y="5" width="11" height="2"/><rect x="0" y="10" width="3" height="2"/><rect x="5" y="10" width="11" height="2"/></g></svg>VIEW INVENTORY
  </a>

  <form class="abs newsletter">
    <div class="newsletter-title">NEWSLETTER SIGNUP</div>
    <div class="newsletter-input">enter your e-mail</div>
    <div class="newsletter-submit">›&nbsp; SUBSCRIBE</div>
  </form>
</section>

<footer>
  <div class="abs site-footer"></div>
  <div class="abs footer-brand">LONE CANYON<br>CYCLE DEPOT</div>
  <ul class="abs footer-links" style="left:270px"><li>News &amp; Events</li><li>Special Promotions</li><li>Newsletter</li></ul>
  <ul class="abs footer-links" style="left:437px"><li>Network Solutions</li><li>Support Forum</li><li>Database Management</li></ul>
  <div class="abs social-row footer-social" aria-label="Social links">
    <span class="social-dot"></span><span class="social-dot"></span><span class="social-dot"></span><span class="social-dot"></span><span class="social-dot"></span>
  </div>
  <div class="abs legal"></div>
  <div class="abs legal-left">T &amp; C&nbsp; and Privacy policy</div>
  <div class="abs legal-right">Copyright © 2014&nbsp; Texas&nbsp; | All Rights reserved .</div>
</footer>

</body>
</html>
```